Business Card Design Project

I need a business card design for my law office. I already have a logo.

I am an employment attorney who represents clients who have been wrongfully terminated or have been discriminated against by their employer.

I would like a unique, clean design using the colors in the logo or colors that complement the logo.

Target Market(s)

Clients, potential clients, other attorneys and others.

Industry/Entity Type

Attorney

Requirements
Must have
• I would like to use both sides of the card.

The information on the card must be easy to read.

Here is my information:

T. Dale Everhoff
3857 E. Pallister Rd., Suite 204
Kestrel, California 93999
559-731-4086
559-862-5143 fax
dale@lawtde.example
Nice to have
• QR Code? I would like to see designs incorporating a nice-looking QR code. Look at this example:

Notice the second QR code in the article - the color.

```html
<!DOCTYPE html>
<html lang="en">
<head>
<meta charset="utf-8">
<title>Everhoff Law Office – Business Card</title>
<link rel="stylesheet" href="https://fonts.googleapis.com/css2?family=Tinos:wght@400&display=swap">
<style>
  :root {
    --backdrop: #b4bca6;
    --card: #ffffff;
    --brand-blue: #1e8fd8;
    --name-blue: #1f4fe0;
    --ink: #111111;
    --shadow: rgba(40, 48, 30, 0.35);
  }
  * { margin: 0; padding: 0; box-sizing: border-box; }
  html, body {
    width: 1200px;
    height: 900px;
    overflow: hidden;
  }
  body {
    background: var(--backdrop);
    font-family: "Tinos", "Times New Roman", serif;
    position: relative;
  }
  .card {
    position: absolute;
    top: 307px;
    width: 500px;
    height: 286px;
    background: var(--card);
    box-shadow: 0 6px 14px var(--shadow);
  }
  .card--front { left: 70px; }
  .card--back { left: 630px; }

  .brand {
    display: flex;
    align-items: center;
    gap: 10px;
    color: var(--brand-blue);
  }
  .brand__mark {
    background: var(--brand-blue);
    flex: none;
  }
  .brand__name { font-weight: 400; white-space: nowrap; }

  .card--front .brand {
    position: absolute;
    left: 26px;
    top: 126px;
  }
  .card--front .brand__mark { width: 26px; height: 26px; }
  .card--front .brand__name { font-size: 17px; }

  .contact {
    position: absolute;
    left: 240px;
    top: 76px;
    color: var(--ink);
    font-size: 15.5px;
    line-height: 21px;
    font-style: normal;
  }
  .contact__name {
    color: var(--name-blue);
    font-size: 18px;
    margin-bottom: 9px;
  }
  .contact__email {
    position: absolute;
    left: 0;
    right: 0;
    top: 228px;
    text-align: center;
    color: var(--ink);
    font-size: 16px;
  }

  .card--back .brand {
    position: absolute;
    left: 50%;
    top: 50%;
    transform: translate(-50%, -50%);
    gap: 14px;
  }
  .card--back .brand__mark { width: 44px; height: 44px; }
  .card--back .brand__name { font-size: 30px; }
</style>
</head>
<body>
  <section class="card card--front" aria-label="Business card front">
    <div class="brand">
      <span class="brand__mark"></span>
      <span class="brand__name">Everhoff Law Office</span>
    </div>
    <address class="contact">
      <p class="contact__name">T. Dale Everhoff</p>
      <p>3857 E. Pallister Rd., Suite 204</p>
      <p>Kestrel, California 93999</p>
      <p>tel: 555-731-4086</p>
      <p>fax: 555-862-5143</p>
    </address>
    <p class="contact__email">dale@lawtde.example</p>
  </section>

  <section class="card card--back" aria-label="Business card back">
    <div class="brand">
      <span class="brand__mark"></span>
      <span class="brand__name">Everhoff Law Office</span>
    </div>
  </section>
</body>
</html>
```